New Business Card Design Project

We are looking for a talented individual to create a truly awesome/unique business card design for us. We are looking for a someone to design something that will really stand out from the crowd - we don't mind what ideas you come up with (ie embossed/flat/matte/shine etc etc) just wow us with your creativity.
Updates

Sick

Target Market(s)

Video Games Industry Professionals (all levels of seniority from QA Testers through to CEOs)

Contact Information for Business Card

Company logo (see upload)
Company name: Northbridge Play Careers Ltd
Employee Name: Harriet Vasko
Job title: CEO
Website: www.npc2go.com
Office +44 1632 960418
Mobile: +44 7700 900582
Email: harriet@npc2go.com

Colors

Designer to choose colors to be used in the design.

Requirements
Must have
• The business card design MUST contain all the information listed in the BUSINESS CARD DETAILS box.
• You will see the colours that are relevant to us (ie company logo) in the uploaded imagery - however you do not have to use all these colours when designing the business card itself
• MUST BE DOUBLE SIDED

```html
<!DOCTYPE html>
<html lang="en">
<head>
<meta charset="UTF-8">
<title>Northbridge Play Careers – Business Card</title>
<link rel="stylesheet" href="https://fonts.googleapis.com/css2?family=Exo+2:wght@600&family=Oswald:wght@500&family=Work+Sans:wght@400&display=swap">
<style>
  :root {
    --backdrop: #202020;
    --card-navy: #1f3264;
    --card-navy-light: #24386e;
    --deboss: #1a2a55;
    --deboss-edge: #2c4280;
    --silver: #e3e6ee;
    --silver-dim: #b9bfcf;
    --rule: #7f89a6;
  }
  * { margin: 0; padding: 0; box-sizing: border-box; }
  html, body {
    width: 1200px;
    height: 900px;
    overflow: hidden;
    background: var(--backdrop);
  }
  .sheet {
    position: relative;
    width: 1200px;
    height: 900px;
    display: flex;
    flex-direction: column;
    align-items: center;
    justify-content: center;
    gap: 40px;
  }
  .card {
    position: relative;
    width: 700px;
    height: 400px;
    background: linear-gradient(135deg, var(--card-navy) 0%, var(--card-navy-light) 100%);
  }

  /* Front */
  .card-front {
    display: flex;
    align-items: center;
    justify-content: center;
    gap: 22px;
  }
  .brand-dot {
    width: 70px;
    height: 70px;
    border-radius: 50%;
    background: var(--deboss);
    box-shadow: inset 1px 1px 0 var(--deboss-edge);
  }
  .brand-name {
    font-family: "Exo 2", sans-serif;
    font-weight: 600;
    font-size: 34px;
    line-height: 1.0;
    letter-spacing: 1px;
    color: var(--silver);
  }

  /* Back */
  .card-back {
    display: flex;
    align-items: center;
    justify-content: center;
  }
  .identity {
    text-align: right;
    padding-right: 34px;
  }
  .person-name {
    font-family: "Oswald", sans-serif;
    font-weight: 500;
    font-size: 44px;
    letter-spacing: 0;
    line-height: 1;
    text-transform: uppercase;
    color: var(--deboss);
    text-shadow: 1px 1px 0 var(--deboss-edge);
  }
  .person-role {
    margin-top: 8px;
    font-family: "Work Sans", sans-serif;
    font-size: 17px;
    letter-spacing: 1px;
    color: var(--deboss);
    text-shadow: 1px 1px 0 var(--deboss-edge);
  }
  .divider {
    width: 1px;
    height: 100px;
    background: var(--rule);
  }
  .contacts {
    list-style: none;
    padding-left: 34px;
  }
  .contacts li {
    display: flex;
    align-items: center;
    gap: 12px;
    font-family: "Work Sans", sans-serif;
    font-size: 19px;
    letter-spacing: 1px;
    line-height: 30px;
    color: var(--silver);
  }
  .contacts svg {
    width: 14px;
    height: 14px;
    flex: none;
    stroke: var(--silver-dim);
    fill: none;
    stroke-width: 1.6;
  }
</style>
</head>
<body>
  <main class="sheet">
    <section class="card card-front" aria-label="Card front">
      <span class="brand-dot"></span>
      <p class="brand-name">Northbridge<br>Play Careers</p>
    </section>

    <section class="card card-back" aria-label="Card back">
      <div class="identity">
        <h1 class="person-name">Harriet Vasko</h1>
        <p class="person-role">CEO</p>
      </div>
      <div class="divider"></div>
      <ul class="contacts">
        <li>
          <svg viewBox="0 0 16 16" aria-hidden="true"><path d="M3 1.5l3 3-1.5 2a8 8 0 0 0 5 5l2-1.5 3 3-2 2C7 15 1 9 1 3.5z"/></svg>
          +44 1632 960418
        </li>
        <li>
          <svg viewBox="0 0 16 16" aria-hidden="true"><rect x="4" y="1" width="8" height="14" rx="1.5"/><line x1="7" y1="12.5" x2="9" y2="12.5"/></svg>
          +44 7700 900582
        </li>
        <li>
          <svg viewBox="0 0 16 16" aria-hidden="true"><rect x="1" y="3" width="14" height="10" rx="1"/><path d="M1 3l7 6 7-6"/></svg>
          harriet@npc2go.com
        </li>
        <li>
          <svg viewBox="0 0 16 16" aria-hidden="true"><circle cx="8" cy="8" r="6.5"/><ellipse cx="8" cy="8" rx="3" ry="6.5"/><line x1="1.5" y1="8" x2="14.5" y2="8"/></svg>
          www.npc2go.com
        </li>
      </ul>
    </section>
  </main>
</body>
</html>
```